Filter Cleaning Business requires an advertisement that can be used on billboards, trucks, magazines

I require an advertisement that can be used wherever required promoting the services of the business in short form attracting the attention of prospective customers and making them want more information.
We also need to promote the companies philosophy to assist business improve and form partnerships in achieving this. Also that the company has proven with existing customers the ability to achieve this.
The company already has a logo and want the ad to align with the logo.

Target Market(s)

The target market is mainly Mining, Construction, Energy and Heavy Industrial companies.

Industry/Entity Type

Business

Requirements
Must have
• The ad must include the company logo
Nice to have
• The ad would include pictures of different kinds of filters serviced by the company.

```html
<!DOCTYPE html>
<html lang="en">
<head>
<meta charset="utf-8">
<title>Southern Filter Renewal Services – Advertisement</title>
<link rel="stylesheet" href="https://fonts.googleapis.com/css2?family=Roboto+Condensed:wght@700&family=Arimo:wght@400;700&family=Michroma&display=swap">
<style>
  :root {
    --page: #ffffff;
    --grey-light: #e3e3df;
    --grey-dark: #9ea3a8;
    --green-bright: #6cbf2a;
    --green-mid: #0f9c3a;
    --green-deep: #0b6b25;
    --green-band: #1d6e17;
    --headline-box: #0c5a1c;
    --yellow: #f5e400;
    --white: #ffffff;
    --ink: #2b2b2b;
    --filter-light: #d9dcd8;
    --filter-dark: #8d948e;
  }
  * { margin: 0; padding: 0; box-sizing: border-box; }
  html, body { width: 1200px; height: 900px; overflow: hidden; background: var(--page); }
  .ad {
    position: absolute; left: 0; top: 25px; width: 1200px; height: 847px;
    overflow: hidden;
    background: linear-gradient(100deg, var(--grey-light) 0%, #c9cac8 45%, var(--grey-dark) 100%);
    font-family: "Arimo", Arial, sans-serif;
  }
  .backdrop { position: absolute; inset: 0; }

  .brand { position: absolute; left: 55px; top: 45px; width: 470px; text-align: center; }
  .brand-dot {
    width: 150px; height: 150px; border-radius: 50%;
    background: var(--green-mid); margin: 0 auto 22px;
  }
  .brand-name {
    font-family: "Michroma", sans-serif; color: var(--ink);
    font-size: 25px; line-height: 32px; letter-spacing: 1px; text-transform: uppercase;
  }

  .headline {
    position: absolute; right: 75px; top: 52px; width: 560px;
    font-family: "Roboto Condensed", sans-serif; font-weight: 700; color: var(--white);
    font-size: 56px; line-height: 56px;
  }
  .headline span {
    display: inline-block; background: var(--headline-box);
    padding: 2px 12px; border-radius: 16px; margin-bottom: 4px;
  }
  .headline .hl { color: var(--yellow); }
  .headline .l1 { margin-left: -65px; }
  .headline .l2 { margin-left: -40px; }
  .headline .l3, .headline .l4 { float: right; clear: right; }
  .headline .l3 { margin-top: 10px; }

  .pitch {
    position: absolute; left: 586px; top: 322px; width: 540px;
    color: var(--white); font-size: 17px; line-height: 20px;
  }

  .benefits, .process { position: absolute; left: 55px; list-style: none; color: var(--white); font-size: 18px; line-height: 27px; }
  .benefits { top: 358px; width: 380px; }
  .process { top: 632px; width: 420px; }
  .benefits li, .process li { position: relative; padding-left: 24px; }
  .benefits li::before, .process li::before {
    content: ""; position: absolute; left: 2px; top: 9px;
    border-left: 7px solid var(--white); border-top: 4px solid transparent; border-bottom: 4px solid transparent;
  }
  .benefits .wrap { line-height: 26px; }

  .process-title {
    position: absolute; left: 55px; top: 604px;
    font-family: "Michroma", sans-serif; font-size: 15px; letter-spacing: 2px;
    color: var(--ink); text-transform: uppercase;
  }

  .filters-photo {
    position: absolute; left: 610px; top: 410px; width: 515px; height: 365px;
    border-radius: 18px 18px 6px 6px;
    background: linear-gradient(160deg, var(--filter-light) 0%, #b9bdb8 55%, var(--filter-dark) 100%);
    opacity: .9;
  }

  .contact-bar {
    position: absolute; left: 0; top: 793px; width: 1200px; height: 54px;
    display: flex; align-items: center; font-size: 21px; color: #111;
  }
  .contact-bar .cta { position: absolute; left: 125px; display: flex; align-items: center; gap: 12px; }
  .contact-bar .phone { position: absolute; left: 495px; }
  .contact-bar .email { position: absolute; left: 795px; }
  .contact-bar strong { color: var(--yellow); font-weight: 700; }
</style>
</head>
<body>
<main class="ad">
  <svg class="backdrop" width="1200" height="847" viewBox="0 0 1200 847" aria-hidden="true">
    <defs>
      <linearGradient id="swoosh" x1="0" y1="0" x2="1" y2="1">
        <stop offset="0" stop-color="#0fa03a"/>
        <stop offset=".55" stop-color="#0c9a36"/>
        <stop offset="1" stop-color="#5fb52a"/>
      </linearGradient>
      <linearGradient id="swoosh-edge" x1="0" y1="0" x2="1" y2="0">
        <stop offset="0" stop-color="#0f9c3a"/>
        <stop offset="1" stop-color="#6cbf2a"/>
      </linearGradient>
    </defs>
    <path d="M0 322 C330 320 760 250 1200 45 L1200 847 L0 847 Z" fill="url(#swoosh-edge)"/>
    <path d="M0 335 C340 335 780 300 1200 110 L1200 847 L0 847 Z" fill="url(#swoosh)"/>
    <path d="M640 793 C820 700 1000 620 1200 520 L1200 793 Z" fill="#1e7a1a" opacity=".85"/>
    <rect x="0" y="793" width="1200" height="54" fill="#1d6e17"/>
    <line x1="75" y1="792" x2="1125" y2="792" stroke="#b7d7a8" stroke-width="1.5"/>
  </svg>

  <header class="brand">
    <div class="brand-dot"></div>
    <p class="brand-name">Southern<br>Filter Renewal Services</p>
  </header>

  <h1 class="headline">
    <span class="l1"><b class="hl">“We can come to you”</b></span><br>
    <span class="l2">to clean your filters!</span>
    <span class="l3">You get <b class="hl">“your”</b> filter</span>
    <span class="l4">returned!</span>
  </h1>

  <p class="pitch">We‘re confident in our company and in our product.<br>We are sure that you will be, too. Contact us today to start saving the environment and start saving money<br>by using recycled filters.</p>

  <ul class="benefits">
    <li>Recycle</li>
    <li>Re-use</li>
    <li>Reduce landfill impact</li>
    <li class="wrap">Save you 40 – 60 % off new filter by recycling your filters</li>
    <li>Reduces operating expenses</li>
    <li>Increase carbon credits</li>
    <li>Reduce Inventory</li>
  </ul>

  <h2 class="process-title">Southern Filter Renewal Services</h2>
  <ul class="process">
    <li>Uses no water or chemicals</li>
    <li>Uses clean air to blow and vacuum</li>
    <li>Inspects every filter for integrity</li>
    <li>Track filter cleaning cycles</li>
    <li>Vacuum tests every filter</li>
  </ul>

  <div class="filters-photo" role="img" aria-label="Photo of a group of cleaned cylindrical industrial air filters with metal mesh casings"></div>

  <footer class="contact-bar">
    <span class="cta">CONTACT US TODAY
      <svg width="38" height="12" viewBox="0 0 38 12" aria-hidden="true"><path d="M0 6 H30" stroke="#f5e400" stroke-width="2.5"/><path d="M26 1 L37 6 L26 11 Z" fill="#f5e400"/></svg>
    </span>
    <span class="phone">Phone <strong>049 555 0142</strong></span>
    <span class="email">Email <strong>info@sfrs.com.au</strong></span>
  </footer>
</main>
</body>
</html>
```